Vardexol with two other company logos

We need a new design for our business cards. We have used the same business cards for more than 10 years. We have now expanded and want to add our other two business logos to incorporate with our original business logo. I have added our current business card (Vardexol) onto here. Also I have added an example of what we would like to see on the business card.

Target Market(s)

Nutritional market

Industry/Entity Type

Business

Contact Information for Business Card

Vardexol, Halvorsen Goods Works, Base relief Product
Will use business cards for Multiple of people in my company.

Colors

Designer to choose colors to be used in the design.

Requirements
Must have
• three logos on my business cards
Nice to have
• something that stands out.

```html
<!DOCTYPE html>
<html lang="en">
<head>
<meta charset="utf-8">
<title>Vardexol Business Card</title>
<link rel="stylesheet" href="https://fonts.googleapis.com/css2?family=Open+Sans:wght@400;600;700&display=swap">
<style>
  :root {
    --backdrop: #d9d8d6;
    --card: #ffffff;
    --ink: #111111;
    --muted: #6f6f6f;
    --accent: #f05a1e;
    --leaf: #7aa152;
    --navy: #1f3f8f;
    --shadow: rgba(0,0,0,0.28);
  }
  * { margin: 0; padding: 0; box-sizing: border-box; }
  html, body {
    width: 1200px; height: 1010px; overflow: hidden;
    background: var(--backdrop);
    font-family: "Open Sans", Arial, sans-serif;
  }
  .stage { position: relative; width: 1200px; height: 1010px; }
  .card {
    position: absolute; left: 250px; width: 700px; height: 400px;
    background: var(--card);
    box-shadow: 4px 6px 10px var(--shadow);
  }
  .card--back { top: 80px; }
  .card--front { top: 530px; }

  .brand-row {
    position: absolute; top: 120px; left: 0; right: 0;
    display: flex; justify-content: space-around; align-items: center;
    padding: 0 60px;
  }
  .brand { display: flex; align-items: center; gap: 10px; font-weight: 700; font-size: 22px; }
  .brand__dot { width: 22px; height: 22px; border-radius: 50%; flex: none; }
  .brand--halvorsen { color: var(--leaf); }
  .brand--halvorsen .brand__dot { background: var(--leaf); }
  .brand--relief { color: var(--navy); }
  .brand--relief .brand__dot { background: var(--navy); }
  .website {
    position: absolute; bottom: 48px; left: 0; right: 0; text-align: center;
    color: var(--muted); font-size: 20px; letter-spacing: 2px;
  }

  .main-brand {
    position: absolute; top: 110px; left: 60px;
    display: flex; align-items: center; gap: 12px;
    color: var(--ink); font-weight: 700; font-size: 48px; letter-spacing: 1px;
  }
  .main-brand__dot { width: 26px; height: 26px; border-radius: 50%; background: var(--accent); }
  .contact { position: absolute; top: 70px; right: 60px; text-align: right; color: var(--muted); }
  .contact__name { color: var(--accent); font-size: 22px; font-weight: 600; }
  .contact__title { font-size: 19px; margin-top: 4px; }
  .contact__lines { margin-top: 34px; font-size: 17px; line-height: 1.45; }
  .address { position: absolute; left: 60px; bottom: 48px; color: var(--muted); font-size: 17px; }
</style>
</head>
<body>
<main class="stage">
  <section class="card card--back">
    <div class="brand-row">
      <div class="brand brand--halvorsen"><span class="brand__dot"></span>Halvorsen Goods Works</div>
      <div class="brand brand--relief"><span class="brand__dot"></span>Base Relief Product</div>
    </div>
    <p class="website">www.vardexol.com</p>
  </section>

  <section class="card card--front">
    <div class="main-brand"><span>Vardexol LLC</span><span class="main-brand__dot"></span></div>
    <div class="contact">
      <p class="contact__name">Dana Whitfield</p>
      <p class="contact__title">Prezident Owner</p>
      <div class="contact__lines">
        <p>P: 555-014-2210</p>
        <p>F: 555-014-2288</p>
        <p>dana@vardexol.com</p>
      </div>
    </div>
    <p class="address">PO Box 418, Fern Hollow, WI 53999</p>
  </section>
</main>
</body>
</html>
```